Collage: Kunden in Coaching und Organisationsberatung

Ich brauche eine jederzeit mit herkömmlichen Programmen bearbeitbare Vorlage, um in sozialen Medien meine Kunden vorstellen zu können - damit zu erklären, wie Coaching und Organisationsberatung wirken kann. Diese Persona sollen in einer Collage mit passenden Bildern und Texten präsentiert werden können. Als grafische Orientierung kann meine Homepage https://www.plavisno.at/ dienen. Meine Farbcodes sind auf der Webseite - sprich digital RGB: Blau: #739fc7, Grün: #b8c830 und Orange: #cc610a; Im Print also CMYK: Blau: 70/20/10/0, Grün: 0/10/100/0 und Orange: 0/68/100/0; Texte sollen in folgender Länge Platz finden - diese Info dient nur zur Größenabschätzung der Platzhalter. Der Rest kann frei mit Bildern, Symbolen, ... gestaltet werden.
Textbeispiel 1:
Helga – Führungskraft mit Ambitionen und Herausforderungen
Alter: 42 Jahre
Funktion: Bereichsleiterin Finanzen in einem großen Dienstleistungsunternehmen
Lebenssituation: Verheiratet, zwei Kinder (Gymnasium, Unterstufe), Partner arbeitet als technischer Zeichner
🎯 Ziele & 🧭 Motive
• Will sich als moderne Führungskraft etablieren – mit Haltung, Vertrauen und Eigenverantwortung
• Strebt eine konstruktive, offene Kommunikation in ihrem Bereich an
• Möchte ihren Managementstil von operativer Detailarbeit hin zur strategischen Führung weiterentwickeln
• Sucht nach Balance zwischen Beruf, Familie und persönlichen Bedürfnissen
⚠️ Herausforderungen & Belastungen
• Übergang von Kollegin zu Vorgesetzter: Beziehungskonflikte und Rollenklarheit
• Kommunikationskultur im Team ist verschlossen und wenig kooperativ
• Hoher Anspruch an sich selbst – und an andere
• Rückfall in operative Aufgaben → Zeitdruck & Energieverlust
• Entscheidungsschwierigkeiten durch komplexe Abstimmungen und fehlende Klarheit über Stakeholder
• Innere Spannung zwischen Führungsanspruch und fehlendem methodischem Rüstzeug
💬 Typische Aussagen
• „Ich will nicht führen wie mein Vorgänger – das geht heute anders.“
• „Ich will, dass die Leute Verantwortung übernehmen und nicht nur ausführen.“
• „Manchmal bin ich zu ungeduldig – aber ich habe einfach keine Zeit für Umwege.“
• „Ich muss weg von der Detailarbeit – aber wie schaffe ich das wirklich?“
📌 Entwicklungsbedarfe
• Coaching zur Selbstklärung und Rollenentwicklung
• Training zu Kommunikation in Führung, Feedback- und Konfliktkultur
• Impulse zur Reflexion über Führungshaltung und Teamsteuerung
• Unterstützung im Aufbau eines kollaborativen Netzwerks innerhalb der Organisation
📣 Zielgruppenansprache (Voxtera-Kontext)
Diese Persona spricht Führungskräfte an, die:
• neu in ihrer Rolle sind (meist durch schnellen Aufstieg)
• den Willen zur Veränderung mitbringen, aber noch nicht das passende Werkzeug
• zwischen strategischem Anspruch und operativem Alltag aufgerieben werden
• Kommunikation, Führung und Selbstführung gleichzeitig lernen und leben wollen
Textbeispiel 2:
Herbert
Persona: Herbert – Fachlich stark, persönlich überfordert
Alter: 36 Jahre
Funktion: Bilanzbuchhalter in einer mittelgroßen Spedition
Position: Formal als Abteilungsleiter geführt – ohne kommunizierte Führungsverantwortung
Lebenssituation: Lebt allein, gelegentliche Beziehungserfahrungen
🎯 Ziele & 🧭 Motive
• Wünscht sich Stabilität, Struktur und fachlich saubere Arbeitsprozesse
• Möchte gute, fehlerfreie Arbeit leisten und professionell wahrgenommen werden
• Hat sich für diesen Job entschieden, um mehr Lebensqualität zu gewinnen
• Sehnt sich nach Klarheit in Rollen, Zuständigkeiten und Abläufen
• Ungeklärte Führungsrolle: Der Titel „Abteilungsleiter*“ verunsichert – es fehlt eine explizite Einordnung
• Überlastung durch chaotische Prozesse und laufende Systemumstellung
• Fehlende Unterstützung im Team – insbesondere durch eine überforderte Kollegin
• Schwierigkeiten, Grenzen zu setzen oder Klarheit einzufordern – v. a. gegenüber Führungskraft und Kolleg*innen
• Perfektionismus führt zu Überstunden, Schlafproblemen und emotionaler Erschöpfung
• Geringe Sichtbarkeit im Betrieb – kaum Kommunikation außerhalb des Büros
• Hohes Bedürfnis nach Kontrolle steht einem agilen Umfeld entgegen
💬 Typische Aussagen
• „Ich bin kein Abteilungsleiter – ich habe das nie gewollt.“
• „Ich will einfach gute Arbeit machen – aber so geht das nicht.“
• „Ich habe keine Zeit, das Chaos zu ordnen – ich bin zu sehr damit beschäftigt, es auszuhalten.“
• „Coaching? Vielleicht bringt es ja wenigstens etwas Struktur in meine Gedanken.“
📌 Entwicklungsbedarfe
• Klärung der eigenen beruflichen Rolle und Abgrenzung zur Führungsverantwortung
• Unterstützung beim Umgang mit Unklarheit und Perfektionismus
• Stärkung der Selbstführung und Kommunikation im System
• Strukturierungshilfen im Arbeitsalltag – Priorisierung, Delegation, Nein-Sagen
• Entlastung durch Reflexion – Reduktion von Selbstüberforderung
• Ermutigung zur Klärung mit Führungskraft (z. B. über ein geleitetes Gespräch oder systemisches Rollenmodell)
Diese Persona spricht Mitarbeiter*innen an, die:
• fachlich sehr kompetent, aber systemisch überfordert sind
• sich in unklaren Rollen- und Erwartungsstrukturen wiederfinden
• zwischen Anspruch und Wirklichkeit leiden
• sich nach Struktur, Sicherheit und professioneller Entlastung sehnen
• Coaching als „letzte Möglichkeit“ sehen, ihre Gedanken zu ordnen und Klarheit zu gewinnen
LG und danke für die Vorschläge

```html
<!DOCTYPE html>
<html lang="de">
<head>
<meta charset="utf-8">
<title>Persona Herbert – plavisno</title>
<link href="https://fonts.googleapis.com/css2?family=Poppins:wght@400;500;600;700;800&display=swap" rel="stylesheet">
<style>
  :root {
    --blue: #739fc7;
    --blue-dark: #5b87b0;
    --orange: #cc610a;
    --green: #b8c830;
    --red: #e0263f;
    --yellow: #f5b70a;
    --ink: #1d1d1f;
    --white: #ffffff;
    --photo-light: #f3f1ee;
    --photo-mid: #e4ddd4;
    --photo-warm: #d9cbbb;
  }
  * { box-sizing: border-box; margin: 0; padding: 0; }
  html, body { width: 878px; height: 1200px; overflow: hidden; background: var(--white); }
  body { font-family: "Poppins", sans-serif; color: var(--ink); position: relative; }

  /* Sidebar */
  .sidebar { position: absolute; left: 43px; top: 0; width: 278px; }
  .portrait {
    height: 346px;
    background: linear-gradient(90deg, var(--photo-light) 0%, var(--photo-mid) 45%, var(--photo-warm) 75%, var(--photo-light) 100%);
  }
  .profile { background: var(--blue); color: var(--white); padding: 42px 20px 0; height: 353px; }
  .profile__name { font-size: 36px; font-weight: 800; letter-spacing: 0.5px; line-height: 1; }
  .profile__tagline { color: var(--ink); font-weight: 600; font-size: 13px; line-height: 1.3; margin-top: 12px; }
  .profile__label { font-weight: 700; font-size: 13.5px; margin-top: 14px; }
  .profile__label span { font-weight: 400; margin-left: 4px; }
  .profile__text { font-size: 13px; line-height: 1.28; margin-top: 4px; }
  .profile__gap { margin-top: 22px; }

  .audience { background: var(--blue); color: var(--white); border-top: 1px solid var(--blue-dark); padding: 34px 16px 0; height: 370px; }
  .audience__title { color: var(--ink); font-weight: 800; font-size: 15.5px; line-height: 1.15; text-transform: uppercase; }
  .audience__intro { font-size: 13.5px; line-height: 1.3; margin-top: 16px; }
  .audience__list { list-style: none; margin-top: 16px; }
  .audience__list li { position: relative; padding-left: 20px; font-size: 11px; line-height: 1.15; margin-bottom: 15px; }
  .audience__list li::before {
    content: "✓"; position: absolute; left: 0; top: 1px; width: 11px; height: 11px; border-radius: 50%;
    background: var(--white); color: var(--blue); font-size: 8px; font-weight: 700; text-align: center; line-height: 11px;
  }

  .brand { position: absolute; left: 43px; top: 1100px; font-size: 40px; font-weight: 600; line-height: 1; color: var(--ink); }

  /* Content */
  .section { position: absolute; left: 350px; width: 496px; }
  .section--goals { top: 56px; }
  .section--challenges { top: 240px; }
  .section--quotes { top: 596px; }
  .section--needs { top: 792px; }
  .section__head { display: flex; align-items: center; gap: 18px; margin-bottom: 14px; }
  .section__icon { width: 34px; height: 34px; flex: none; }
  .section__title { font-weight: 800; font-size: 23px; line-height: 1.08; text-transform: uppercase; }

  .bullets { list-style: none; padding-left: 18px; }
  .bullets li { position: relative; padding-left: 18px; }
  .bullets li::before {
    content: "✓"; position: absolute; left: 0; top: 3px; width: 10px; height: 10px; border-radius: 50%;
    background: var(--orange); color: var(--white); font-size: 7px; font-weight: 700; text-align: center; line-height: 10px;
  }
  .bullets--small li { font-size: 11.2px; line-height: 1.25; margin-bottom: 14px; }
  .bullets--medium li { font-size: 13px; line-height: 1.25; margin-bottom: 11px; }

  .quotes { list-style: none; padding-left: 18px; }
  .quotes li { font-size: 13px; line-height: 1.0; margin-bottom: 13px; padding-left: 18px; position: relative; }
  .quotes li::before, .quotes .close { color: var(--blue); font-weight: 800; font-size: 22px; line-height: 0; font-family: Georgia, serif; }
  .quotes li::before { content: "“"; position: absolute; left: 0; top: 10px; }
  .quotes .close { position: relative; top: 8px; margin-left: 4px; }
  .needs__lead { font-weight: 700; font-size: 12.6px; padding-left: 36px; margin-bottom: 12px; }

  /* Contact */
  .contact { position: absolute; left: 364px; top: 1120px; display: flex; align-items: center; gap: 34px; font-size: 13px; }
  .contact__item { display: flex; align-items: center; gap: 14px; }
  .contact__icon { width: 22px; height: 22px; border-radius: 50%; background: var(--blue); display: flex; align-items: center; justify-content: center; }
</style>
</head>
<body>
  <aside class="sidebar">
    <div class="portrait" role="img" aria-label="Platz für Porträtfoto der Persona: Mann im weißen Hemd, an eine helle Wand gelehnt"></div>
    <section class="profile">
      <h1 class="profile__name">HERBERT</h1>
      <p class="profile__tagline">Persona: Herbert – Fachlich stark, persönlich überfordert</p>
      <p class="profile__label">ALTER <span>36 JAHRE</span></p>
      <p class="profile__label">POSITION</p>
      <p class="profile__text">Formal als Abteilungsleiter geführt – ohne kommunizierte Führungsverantwortung</p>
      <p class="profile__label profile__gap">LEBENSSITUATION</p>
      <p class="profile__text">Lebt allein, gelegentliche Beziehungserfahrungen</p>
    </section>
    <section class="audience">
      <h2 class="audience__title">Zielgruppenansprache (Voxtera-Kontext)</h2>
      <p class="audience__intro">Diese Persona spricht Mitarbeiter*innen an, die:</p>
      <ul class="audience__list">
        <li>fachlich sehr kompetent, aber systemisch überfordert sind</li>
        <li>sich in unklaren Rollen- und Erwartungsstrukturen wiederfinden</li>
        <li>zwischen Anspruch und Wirklichkeit leiden</li>
        <li>sich nach Struktur, Sicherheit und professioneller Entlastung sehnen</li>
        <li>Coaching als „letzte Möglichkeit“ sehen, ihre Gedanken zu ordnen und Klarheit zu gewinnen</li>
      </ul>
    </section>
  </aside>

  <div class="brand">plavisno</div>

  <section class="section section--goals">
    <div class="section__head">
      <svg class="section__icon" viewBox="0 0 36 36" aria-hidden="true">
        <circle cx="17" cy="19" r="15" fill="var(--red)"/>
        <circle cx="17" cy="19" r="10" fill="var(--white)"/>
        <circle cx="17" cy="19" r="5.5" fill="var(--red)"/>
        <line x1="17" y1="19" x2="30" y2="6" stroke="#555" stroke-width="2"/>
        <circle cx="30" cy="6" r="3" fill="var(--yellow)"/>
      </svg>
      <h2 class="section__title">Ziele &amp; Motive</h2>
    </div>
    <ul class="bullets bullets--small">
      <li>Wünscht sich Stabilität, Struktur und fachlich saubere Arbeitsprozesse</li>
      <li>Möchte gute, fehlerfreie Arbeit leisten und professionell wahrgenommen werden</li>
      <li>Hat sich für diesen Job entschieden, um mehr Lebensqualität zu gewinnen</li>
      <li>Sehnt sich nach Klarheit in Rollen, Zuständigkeiten und Abläufen</li>
    </ul>
  </section>

  <section class="section section--challenges">
    <div class="section__head">
      <svg class="section__icon" viewBox="0 0 36 36" aria-hidden="true">
        <circle cx="18" cy="18" r="15" fill="#fbd46a"/>
        <circle cx="18" cy="18" r="15" fill="none" stroke="var(--blue)" stroke-width="1.5" stroke-dasharray="6 4"/>
        <path d="M18 9 L27 25 L9 25 Z" fill="var(--red)"/>
        <rect x="17" y="14" width="2" height="6" fill="var(--white)"/>
        <rect x="17" y="21.5" width="2" height="2" fill="var(--white)"/>
      </svg>
      <h2 class="section__title">Herausforderungen<br>&amp; Belastungen</h2>
    </div>
    <ul class="bullets bullets--medium">
      <li>Ungeklärte Führungsrolle: Der Titel „Abteilungsleiter*“ verunsichert – es fehlt eine explizite Einordnung</li>
      <li>Überlastung durch chaotische Prozesse und laufende Systemumstellung</li>
      <li>Fehlende Unterstützung im Team – insbesondere durch eine überforderte Kollegin</li>
      <li>Schwierigkeiten, Grenzen zu setzen oder Klarheit einzufordern – v. a. gegenüber Führungskraft und Kolleg*innen</li>
      <li>Perfektionismus führt zu Überstunden, Schlafproblemen und emotionaler Erschöpfung</li>
      <li>Geringe Sichtbarkeit im Betrieb – kaum Kommunikation außerhalb des Büros</li>
      <li>Hohes Bedürfnis nach Kontrolle steht einem agilen Umfeld entgegen</li>
    </ul>
  </section>

  <section class="section section--quotes">
    <div class="section__head">
      <svg class="section__icon" viewBox="0 0 36 36" aria-hidden="true">
        <rect x="6" y="3" width="24" height="30" rx="2" fill="var(--white)" stroke="var(--ink)" stroke-width="1.6"/>
        <line x1="10" y1="14" x2="26" y2="14" stroke="var(--ink)" stroke-width="1.4"/>
        <line x1="10" y1="19" x2="26" y2="19" stroke="var(--ink)" stroke-width="1.4"/>
        <line x1="10" y1="24" x2="26" y2="24" stroke="var(--ink)" stroke-width="1.4"/>
        <rect x="3" y="16" width="4" height="14" rx="1" fill="var(--yellow)" stroke="var(--ink)" stroke-width="1"/>
      </svg>
      <h2 class="section__title">Typische Aussagen</h2>
    </div>
    <ul class="quotes">
      <li>Ich bin kein Abteilungsleiter – ich habe das nie gewollt.<span class="close">”</span></li>
      <li>Ich will einfach gute Arbeit machen – aber so geht das nicht<span class="close">”</span></li>
      <li>Ich habe keine Zeit, das Chaos zu ordnen – ich bin zu sehr damit beschäftigt, es auszuhalten.<span class="close">”</span></li>
      <li>Coaching? Vielleicht bringt es ja wenigstens etwas Struktur in meine Gedanken<span class="close">”</span></li>
    </ul>
  </section>

  <section class="section section--needs">
    <div class="section__head">
      <svg class="section__icon" viewBox="0 0 36 36" aria-hidden="true">
        <rect x="4" y="24" width="5" height="9" fill="var(--yellow)"/>
        <rect x="11" y="19" width="5" height="14" fill="var(--green)"/>
        <rect x="18" y="22" width="5" height="11" fill="var(--blue)"/>
        <rect x="25" y="15" width="5" height="18" fill="var(--green)"/>
        <polyline points="4,18 12,11 19,14 31,4" fill="none" stroke="var(--red)" stroke-width="2"/>
        <line x1="2" y1="34" x2="34" y2="34" stroke="var(--blue-dark)" stroke-width="1.5"/>
      </svg>
      <h2 class="section__title">Entwicklungsbedarfe</h2>
    </div>
    <p class="needs__lead">Diese Persona spricht Mitarbeiter*innen an, die:</p>
    <ul class="bullets bullets--medium">
      <li>Klärung der eigenen beruflichen Rolle und Abgrenzung zur Führungsverantwortung</li>
      <li>Unterstützung beim Umgang mit Unklarheit und Perfektionismus</li>
      <li>Stärkung der Selbstführung und Kommunikation im System</li>
      <li>Strukturierungshilfen im Arbeitsalltag – Priorisierung, Delegation, Nein-Sagen</li>
      <li>Entlastung durch Reflexion – Reduktion von Selbstüberforderung</li>
      <li>Ermutigung zur Klärung mit Führungskraft (z. B. über ein geleitetes Gespräch oder systemisches Rollenmodell)</li>
    </ul>
  </section>

  <footer class="contact">
    <div class="contact__item">
      <span class="contact__icon">
        <svg width="12" height="12" viewBox="0 0 24 24" aria-hidden="true"><path fill="#fff" d="M6.6 10.8a15 15 0 0 0 6.6 6.6l2.2-2.2c.3-.3.7-.4 1-.2 1.1.4 2.3.6 3.6.6.6 0 1 .4 1 1V20c0 .6-.4 1-1 1A17 17 0 0 1 3 4c0-.6.4-1 1-1h3.5c.6 0 1 .4 1 1 0 1.3.2 2.5.6 3.6.1.3 0 .7-.2 1z"/></svg>
      </span>
      <span>+43 (0) 660 5182437</span>
    </div>
    <div class="contact__item">
      <span class="contact__icon">
        <svg width="14" height="14" viewBox="0 0 24 24" aria-hidden="true" fill="none" stroke="#fff" stroke-width="1.6"><circle cx="12" cy="12" r="9"/><ellipse cx="12" cy="12" rx="4" ry="9"/><line x1="3" y1="12" x2="21" y2="12"/></svg>
      </span>
      <span>lena.aurhof@plavisno.at</span>
    </div>
  </footer>
</body>
</html>
```